Product Introduction Brochure

Brochure to introduce our mid/high end lighting products to potential wholesalers / Disrtibutors / Retailers. To be mainly graphical but will contain some text also. The purpose of the brochure will be to get potential customers to find out more either by calling us or to visit our website. The brochure should be of A3 size folded in half to an A4. Front page should be mainly logo and name, inner 2 pages should showcase some of the products we can supply together with some text (to be supplied, please use filler text in the initial design), then the back page containing our contact details. The products are lights, floor lamps and table lamps. I have attached a number of images, as well as our company logo. I would prefer the design to be on a black background, however this is not critical
Retailer, distribution and wholesale buyers
Interior design consultants and specifiers
Product

```html
<!DOCTYPE html>
<html lang="en">
<head>
<meta charset="utf-8">
<title>Brighten Your Day – Lighting Brochure Spread</title>
<link rel="stylesheet" href="https://fonts.googleapis.com/css2?family=Josefin+Slab:wght@200;300&family=Josefin+Sans:wght@400&family=Montserrat:wght@700&display=swap">
<style>
  :root {
    --backdrop: #e4e4e4;
    --page: #0b0b0b;
    --page-edge: #1a1a1a;
    --accent: #e8962e;
    --title-light: #f2f2f2;
    --body-text: #d8d8d8;
    --shade-hi: #f4f2ee;
    --shade-lo: #9c9a96;
    --leader: #e8962e;
  }
  * { box-sizing: border-box; margin: 0; padding: 0; }
  html, body { width: 1200px; height: 847px; overflow: hidden; }
  body { background: var(--backdrop); position: relative; font-family: "Josefin Sans", sans-serif; }

  .spread { position: absolute; left: 63px; top: 44px; width: 1074px; height: 759px; display: flex; box-shadow: 0 12px 40px rgba(0,0,0,.25); }
  .page { position: relative; width: 537px; height: 759px; background: linear-gradient(135deg, var(--page-edge), var(--page) 55%); overflow: hidden; }
  .page--left { border-right: 1px solid #2a2a2a; }

  .headline { position: absolute; left: 44px; top: 58px; font-family: "Josefin Slab", serif; font-weight: 200; font-size: 60px; line-height: 1.05; letter-spacing: .2em; text-transform: uppercase; }
  .headline__accent { color: var(--accent); display: block; }
  .headline__main { color: var(--title-light); display: block; }

  .product-photo { background: radial-gradient(ellipse at 35% 35%, var(--shade-hi), var(--shade-lo) 80%); }
  .photo-slot { position: absolute; }

  .product-row { position: absolute; left: 26px; right: 26px; top: 270px; display: flex; gap: 22px; }
  .product-card { flex: 1; text-align: center; }
  .product-card .product-photo { margin: 0 auto 26px; height: 170px; }
  .shape-egg { width: 96px; border-radius: 48% 48% 46% 46%; }
  .shape-oval { width: 140px; height: 130px !important; margin-top: 40px !important; border-radius: 50%; }
  .shape-tall { width: 62px; border-radius: 40% 40% 30% 30%; }

  .product-name { font-family: "Montserrat", sans-serif; font-weight: 700; font-size: 10px; letter-spacing: .22em; color: var(--accent); text-transform: uppercase; margin-bottom: 8px; }
  .product-copy { font-size: 9.5px; line-height: 1.6; color: var(--body-text); }
  .product-price { font-size: 9.5px; color: var(--body-text); margin-top: 6px; }
  .product-price strong { color: var(--accent); font-weight: 400; }

  .feature { position: absolute; text-align: center; width: 180px; }
  .leader { position: absolute; border-color: var(--leader); border-style: dashed; border-width: 0; }
</style>
</head>
<body>
  <main class="spread">
    <section class="page page--left">
      <h1 class="headline">
        <span class="headline__accent">Brighten</span>
        <span class="headline__main">Your Day</span>
      </h1>

      <div class="product-row">
        <article class="product-card">
          <div class="product-photo shape-egg" role="img" aria-label="Photo of a white woven egg-shaped pendant lamp"></div>
          <h2 class="product-name">Lamp's Title</h2>
          <p class="product-copy">Soft woven shade on a slim steel stem gives a warm, even glow for lobbies, dining rooms and quiet corners. Easy to fit, built to last, and sold in trade packs for stockists. Shades come in white, sand and smoke, with matching ceiling cups.</p>
          <p class="product-price">Price: <strong>$29.99</strong></p>
        </article>
        <article class="product-card">
          <div class="product-photo shape-oval" role="img" aria-label="Photo of a wide white woven oval pendant lamp"></div>
          <h2 class="product-name">The Great Title</h2>
          <p class="product-copy">Soft woven shade on a slim steel stem gives a warm, even glow for lobbies, dining rooms and quiet corners. Easy to fit, built to last, and sold in trade packs for stockists. Shades come in white, sand and smoke, with matching ceiling cups.</p>
          <p class="product-price">Price: <strong>$9.99</strong></p>
        </article>
        <article class="product-card">
          <div class="product-photo shape-tall" role="img" aria-label="Photo of a tall slender white pendant lamp"></div>
          <h2 class="product-name">Title</h2>
          <p class="product-copy">Soft woven shade on a slim steel stem gives a warm, even glow for lobbies, dining rooms and quiet corners. Easy to fit, built to last, and sold in trade packs for stockists. Shades come in white, sand and smoke, with matching ceiling cups.</p>
          <p class="product-price">Price: <strong>$19.99</strong></p>
        </article>
      </div>
    </section>

    <section class="page page--right">
      <article class="feature" style="left:170px; top:60px;">
        <h2 class="product-name">Lamp's Name</h2>
        <p class="product-copy">Soft woven shade on a slim steel stem gives a warm, even glow for lobbies, dining rooms and quiet corners. Easy to fit, built to last, and sold in trade packs for stockists. Shades come in white, sand and smoke, with matching ceiling cups.</p>
        <p class="product-price">Price: <strong>$29.99</strong></p>
      </article>
      <div class="leader" style="left:355px; top:150px; width:45px; border-top-width:1px;"></div>
      <div class="photo-slot product-photo" style="left:405px; top:40px; width:100px; height:230px; border-radius:40px 40px 8px 8px;" role="img" aria-label="Photo of a floor lamp with a white egg shade on a curved tripod stand"></div>

      <article class="feature" style="left:30px; top:195px;">
        <h2 class="product-name">Lamp's Name</h2>
        <p class="product-copy">Soft woven shade on a slim steel stem gives a warm, even glow for lobbies, dining rooms and quiet corners. Easy to fit, built to last, and sold in trade packs for stockists. Shades come in white, sand and smoke, with matching ceiling cups.</p>
        <p class="product-price">Price: <strong>$29.99</strong></p>
      </article>
      <div class="leader" style="left:120px; top:395px; height:45px; border-left-width:1px;"></div>
      <div class="photo-slot product-photo" style="left:60px; top:450px; width:120px; height:170px; border-radius:50% 50% 10px 10px;" role="img" aria-label="Photo of a table lamp with a white woven shade on a dark stem"></div>

      <div class="photo-slot product-photo" style="left:215px; top:330px; width:120px; height:240px; border-radius:40px 40px 8px 8px;" role="img" aria-label="Photo of a floor lamp with a tall white shade hanging from a tripod stand"></div>
      <div class="leader" style="left:340px; top:430px; width:30px; border-top-width:1px;"></div>
      <article class="feature" style="left:345px; top:335px;">
        <h2 class="product-name">Lamp's Name</h2>
        <p class="product-copy">Soft woven shade on a slim steel stem gives a warm, even glow for lobbies, dining rooms and quiet corners. Easy to fit, built to last, and sold in trade packs for stockists. Shades come in white, sand and smoke, with matching ceiling cups.</p>
        <p class="product-price">Price: <strong>$29.99</strong></p>
      </article>
    </section>
  </main>
</body>
</html>
```